Wren's Hearth Support Business Card

Business card design
Font must be in Poppins Regular for Wren's Hearth Support
Safe Days Ahead font is Alex Brush

Colour must be Hex #910E2B
RGB 145-14-43
Pantone 7427 C
We want the card editable
On the front please include
Name eg Mavis Dunleavy
Position eg Clinical Care Manager
Phone number mobile 0473 856 342
Phone 08 7394 2650
Email : mavis@wrenshearthsupport.com.au
Address : Gullwing Cove, Western Australia, 6418
Website : wrenshearthsupport.com.au
Contact us today to experience the warmth, respect and personal touch of Wren's Hearth Support.

Target Market(s)

35+

Industry/Entity Type

aged care / community

Contact Information for Business Card

see project description

Requirements
Must have
• Colours, logos and fonts as detailed and uploaded

```html
<!DOCTYPE html>
<html lang="en">
<head>
<meta charset="utf-8">
<title>Wren's Hearth Support Business Card</title>
<link rel="stylesheet" href="https://fonts.googleapis.com/css2?family=Alex+Brush&family=Poppins:wght@400;600&display=swap">
<style>
  :root {
    --brand: #910E2B;
    --paper: #FFFFFF;
    --backdrop: #EEF0F1;
  }
  * { margin: 0; padding: 0; box-sizing: border-box; }
  html, body { width: 1200px; height: 1000px; overflow: hidden; }
  body {
    background: var(--backdrop);
    font-family: "Poppins", sans-serif;
    position: relative;
  }
  .card {
    position: absolute;
    left: 293px;
    width: 615px;
    height: 353px;
    border-radius: 30px;
    overflow: hidden;
  }
  .card--front { top: 100px; background: var(--brand); color: var(--paper); }
  .card--back { top: 527px; background: var(--paper); color: var(--brand); }

  .brand-lockup {
    position: absolute;
    left: 0;
    right: 0;
    top: 110px;
    text-align: center;
  }
  .brand-lockup__name {
    font-weight: 400;
    font-size: 40px;
    line-height: 44px;
    color: var(--paper);
  }
  .brand-lockup__tagline {
    font-family: "Alex Brush", cursive;
    font-size: 30px;
    line-height: 34px;
    margin-top: 4px;
    color: var(--paper);
  }
  .front-message {
    position: absolute;
    left: 0;
    right: 0;
    top: 288px;
    text-align: center;
    font-size: 13.5px;
    line-height: 17px;
  }
  .front-message strong { font-weight: 600; }

  .contact-block { position: absolute; left: 67px; top: 67px; }
  .contact-block__name { font-weight: 600; font-size: 22px; line-height: 28px; }
  .contact-block__role {
    font-size: 9.5px;
    letter-spacing: 3.2px;
    text-transform: uppercase;
    line-height: 12px;
  }
  .contact-block__address {
    margin-top: 24px;
    font-size: 15.5px;
    line-height: 19px;
    font-style: normal;
  }
  .contact-block__lines { margin-top: 19px; list-style: none; font-size: 15.5px; line-height: 19.5px; }
  .contact-block__lines li { display: flex; align-items: center; gap: 5px; }
  .contact-block__lines svg { width: 13px; height: 13px; fill: var(--brand); flex: none; }
  .contact-block__web { margin-top: 19px; font-size: 15.5px; line-height: 19px; }
  .contact-block__web strong { font-weight: 600; }
</style>
</head>
<body>
  <section class="card card--front">
    <div class="brand-lockup">
      <div class="brand-lockup__name">Wren's Hearth<br>Support</div>
      <div class="brand-lockup__tagline">Safe Days Ahead</div>
    </div>
    <p class="front-message">Contact us today to experience the warmth, respect<br>and personal touch of <strong>Wren's Hearth Support</strong>.</p>
  </section>

  <section class="card card--back">
    <div class="contact-block">
      <h1 class="contact-block__name">Mavis Dunleavy</h1>
      <p class="contact-block__role">Clinical Care Manager</p>
      <address class="contact-block__address">Gullwing Cove,<br>Western Australia<br>6418</address>
      <ul class="contact-block__lines">
        <li><svg viewBox="0 0 16 16" aria-hidden="true"><path d="M4 0h8a1.5 1.5 0 0 1 1.5 1.5v13A1.5 1.5 0 0 1 12 16H4a1.5 1.5 0 0 1-1.5-1.5v-13A1.5 1.5 0 0 1 4 0zm0 1.5v13h8v-13zM8 12a1 1 0 1 1 0 2 1 1 0 0 1 0-2z"/></svg>0473 856 342</li>
        <li><svg viewBox="0 0 16 16" aria-hidden="true"><path d="M3.6 1 6 3.6 4.8 5.6a9 9 0 0 0 5.6 5.6l2-1.2L15 12.4l-1.4 2.2C7.4 15 1 8.6 1.4 2.4z"/></svg>08 7394 2650</li>
        <li><svg viewBox="0 0 16 16" aria-hidden="true"><path d="M1 3h14v10H1zm1.2 1.2L8 8.6l5.8-4.4z"/></svg>mavis@wrenshearthsupport.com.au</li>
      </ul>
      <p class="contact-block__web"><strong>wrenshearthsupport</strong>.com.au</p>
    </div>
  </section>
</body>
</html>
```